Simple and clean webdesign for personal homepage

Trying to create a simple and clean webdesign for my personal homepage. Going to use a static site builder with templates to build the site. I want it to have multiple pages - like an about me, blog and resume. I just need something very basic I can customize. I want the main colors to be purple, black and white. I am open to other color palettes too but since purple is my favorite color I want that to be one of the main colors.

The site be mostly text driven. Might have some images in the body text but I want the site design to be light and lean.

Industry/Entity Type

Personal Homepage.

Coding

Coded - Design and coding required

Number of Pages Required

1 page

Font styles to use
Sans Serif

Colors
6B429C
8869AF
B7A5CE
E3DAEB
F3F0F8

Requirements
Must have
• Clean design. Purple used as a color. HTML template.
Nice to have
• Responsive

```html
<!DOCTYPE html>
<html lang="en">
<head>
<meta charset="utf-8">
<title>Violet Vale — Personal Homepage</title>
<link href="https://fonts.googleapis.com/css2?family=Fira+Sans:wght@400;500;600;700&family=Roboto:wght@400;500&display=swap" rel="stylesheet">
<style>
:root{
  --purple:#6B429C;
  --purple-mid:#8869AF;
  --purple-soft:#B7A5CE;
  --lilac:#E3DAEB;
  --mist:#F3F0F8;
  --ink:#111;
  --grey:#666;
  --white:#fff;
}
*{margin:0;padding:0;box-sizing:border-box}
html,body{width:1200px;height:2878px;overflow:hidden}
body{position:relative;font-family:"Fira Sans",sans-serif;color:var(--ink);background:var(--white)}
.abs{position:absolute}

/* hero */
.hero{position:absolute;left:0;top:0;width:1200px;height:557px;background:var(--lilac);overflow:hidden}
.hero-shape{position:absolute;inset:0}
.brand{left:112px;top:28px;font-size:26px;font-weight:500;color:var(--purple)}
.nav{right:112px;top:33px;display:flex;gap:25px}
.nav a{color:var(--white);text-decoration:none;font-size:17px;font-weight:500}
.portrait-ring{left:178px;top:136px;width:358px;height:358px;border-radius:50%;background:#f1f1f1}
.portrait{left:194px;top:152px;width:326px;height:326px;border-radius:50%;background:radial-gradient(circle at 50% 40%,#b9b2a8 0%,#8a8178 45%,#2c2a28 100%)}
.hello{left:577px;top:177px;font-size:21px;font-weight:500;color:var(--white)}
.hero-title{left:575px;top:208px;font-size:47px;font-weight:600;color:var(--white)}
.hero-text{left:578px;top:289px;width:510px;font-size:15.5px;line-height:25px;color:var(--white);text-align:justify}
.btn-contact{left:582px;top:389px;width:141px;height:45px;border-radius:23px;background:var(--white);color:var(--ink);font-size:18px;font-weight:500;display:flex;align-items:center;justify-content:center}

/* section titles */
.sec-title{font-size:31px;font-weight:600;color:var(--purple);border-bottom:2px solid var(--purple);line-height:1.1}
.resume-title{left:542px;top:604px}
.col-head{font-size:26px;font-weight:500;color:var(--ink);border-bottom:2px solid var(--purple);line-height:1.15}

.entry{position:absolute;width:460px}
.entry-top{display:flex;align-items:center;gap:10px}
.year{width:100px;height:36px;border:2px solid var(--purple);border-radius:18px;display:flex;align-items:center;justify-content:center;font-size:21px;font-weight:500}
.place{font-size:17px}
.role{margin:13px 0 0 31px;font-size:26px;font-weight:500;color:var(--purple)}
.desc{margin:8px 0 0 34px;width:410px;font-size:14.5px;line-height:21.5px;text-align:justify;color:#222}

/* portfolio */
.portfolio{position:absolute;left:0;top:1344px;width:1200px;height:512px;background:var(--lilac)}
.port-head{left:118px;top:28px;font-size:26px;font-weight:500;line-height:1.2}
.port-head span{position:absolute;left:0;bottom:-4px;width:54px;height:2px;background:var(--purple)}
.arrow{top:31px;width:31px;height:33px;border:1px solid #333;display:flex;align-items:center;justify-content:center}
.shot{top:105px;width:470px;height:271px;border-radius:20px}
.shot-a{left:112px;background:linear-gradient(135deg,#c58a5a 0%,#8f6a52 45%,#5f7a94 100%)}
.shot-b{left:617px;background:linear-gradient(135deg,#d7d0c2 0%,#9a8f80 45%,#5a6b66 100%)}
.post-date{top:386px;font-size:17px}
.post-title{top:411px;font-size:21.5px;font-weight:600;color:var(--purple)}

/* blog */
.blog-title{left:0;width:1222px;top:1929px;text-align:center;font-size:27px;font-weight:500;color:var(--purple)}
.blog-sub{left:0;width:1245px;top:1974px;text-align:center;font-size:15px;color:#444;font-family:"Roboto",sans-serif}
.card{top:2046px;width:309px;height:242px;background:var(--white);box-shadow:0 0 6px rgba(107,66,156,.28);padding:0 18px;font-family:"Roboto",sans-serif}
.card-date{margin-top:29px;display:flex;align-items:center;gap:15px;font-size:14.5px;color:#555}
.card-title{margin-top:15px;font-size:20.5px;line-height:26px;color:var(--ink)}
.card-text{margin-top:13px;font-size:14.5px;line-height:26px;color:#666}
.card-link{display:inline-block;margin-top:11px;font-size:15px;font-weight:500;color:#333;text-decoration:underline;text-decoration-color:var(--purple);text-underline-offset:3px}

/* contact */
.contact{position:absolute;left:0;top:2357px;width:1200px;height:428px;background:var(--purple-mid);color:var(--white)}
.info{left:161px;width:352px}
.info h4{font-size:21px;font-weight:600}
.info p{margin-top:6px;font-size:20px;line-height:29px;text-align:justify}
.icon{left:111px}
.form-title{left:555px;top:56px;font-size:25px;font-weight:600}
.field{border:1px solid #d9cfe8;font-size:12.5px;padding:0 13px;display:flex;align-items:center;font-family:"Roboto",sans-serif}
.field.tall{align-items:flex-start;padding-top:12px}
.send{left:746px;top:331px;width:149px;height:44px;border-radius:22px;background:var(--purple);display:flex;align-items:center;justify-content:center;font-size:15px;font-weight:600}

/* footer */
.footer{position:absolute;left:0;top:2785px;width:1200px;height:93px;background:var(--purple);color:var(--white);font-weight:600;font-size:15px}
</style>
</head>
<body>

<header class="hero">
  <svg class="hero-shape" width="1200" height="557" viewBox="0 0 1200 557" aria-hidden="true">
    <polygon points="337,0 1200,0 1200,557 515,557" fill="#6B429C"/>
  </svg>
  <div class="abs brand">Violet Vale</div>
  <nav class="abs nav"><a href="#">About Me</a><a href="#">Resume</a><a href="#">Portfolio</a><a href="#">Blog</a><a href="#">Contact</a></nav>
  <div class="abs portrait-ring"></div>
  <div class="abs portrait" role="img" aria-label="Portrait photo of the site owner in a grey suit, arms crossed"></div>
  <div class="abs hello">Hello Its Me</div>
  <h1 class="abs hero-title">Violet Vale</h1>
  <p class="abs hero-text">Nemo enim ipsam voluptatem quia voluptas sit aspernatur aut odit aut fugit, sed quia consequuntur magni dolores eos qui ratione voluptatem sequi nesciunt.</p>
  <div class="abs btn-contact">Contact</div>
</header>

<h2 class="abs sec-title resume-title">Resume</h2>
<h3 class="abs col-head" style="left:110px;top:674px">Education</h3>
<h3 class="abs col-head" style="left:638px;top:674px">Experience</h3>

<div class="entry" style="left:111px;top:733px">
  <div class="entry-top"><span class="year">2009</span><span class="place">University of Studies</span></div>
  <div class="role">UI Design</div>
  <p class="desc">Duis posuere, quam non imperdiet egestas, eros enim mattis mauris, in posuere lacus arcu quis felis. Etiam interdum erat non enim venenatis fermentum.</p>
</div>
<div class="entry" style="left:111px;top:921px">
  <div class="entry-top"><span class="year">2008</span><span class="place">University of Studies</span></div>
  <div class="role">Graphic Design</div>
  <p class="desc">Duis posuere, quam non imperdiet egestas, eros enim mattis mauris, in posuere lacus arcu quis felis. Etiam interdum erat non enim venenatis fermentum.</p>
</div>
<div class="entry" style="left:111px;top:1119px">
  <div class="entry-top"><span class="year">2007</span><span class="place">University of Studies</span></div>
  <div class="role">Frontend Development</div>
  <p class="desc">Duis posuere, quam non imperdiet egestas, eros enim mattis mauris, in posuere lacus arcu quis felis. Etiam interdum erat non enim venenatis fermentum.</p>
</div>
<div class="entry" style="left:639px;top:733px">
  <div class="entry-top"><span class="year">2010</span><span class="place">Bright Harbor</span></div>
  <div class="role">Lead UI/UX Designer</div>
  <p class="desc">Duis posuere, quam non imperdiet egestas, eros enim mattis mauris, in posuere lacus arcu quis felis. Etiam interdum erat non enim venenatis fermentum.</p>
</div>
<div class="entry" style="left:639px;top:921px">
  <div class="entry-top"><span class="year">2015</span><span class="place">Copperleaf Goods</span></div>
  <div class="role">Senior UI/UX Designer</div>
  <p class="desc">Duis posuere, quam non imperdiet egestas, eros enim mattis mauris, in posuere lacus arcu quis felis. Etiam interdum erat non enim venenatis fermentum.</p>
</div>
<div class="entry" style="left:639px;top:1119px">
  <div class="entry-top"><span class="year">2022</span><span class="place">Northwind Labs</span></div>
  <div class="role">Junior UI/UX Designer</div>
  <p class="desc">Duis posuere, quam non imperdiet egestas, eros enim mattis mauris, in posuere lacus arcu quis felis. Etiam interdum erat non enim venenatis fermentum.</p>
</div>

<section class="portfolio">
  <h3 class="abs port-head">Portfolio<span></span></h3>
  <div class="abs arrow" style="left:1013px"><svg width="10" height="12" viewBox="0 0 10 12"><path d="M7 1 2 6l5 5" fill="none" stroke="#6B429C" stroke-width="1.5"/></svg></div>
  <div class="abs arrow" style="left:1055px"><svg width="10" height="12" viewBox="0 0 10 12"><path d="M3 1l5 5-5 5" fill="none" stroke="#6B429C" stroke-width="1.5"/></svg></div>
  <div class="abs shot shot-a" role="img" aria-label="Photo of two colleagues looking at a tablet together"></div>
  <div class="abs shot shot-b" role="img" aria-label="Photo of a team meeting around a table with laptops and a chart"></div>
  <div class="abs post-date" style="left:112px">05 Jan2022</div>
  <div class="abs post-date" style="left:617px">05 Jan2022</div>
  <div class="abs post-title" style="left:110px">Creative and Innovative Navigation Designs</div>
  <div class="abs post-title" style="left:615px">6 Easy Steps to Better Icon Design</div>
</section>

<h2 class="abs blog-title">Latest Blog</h2>
<p class="abs blog-sub">Sed ut perspiciatis unde omnis iste natus error sit voluptatem</p>

<article class="abs card" style="left:112px">
  <div class="card-date"><svg width="13" height="13" viewBox="0 0 13 13"><circle cx="6.5" cy="6.5" r="5.3" fill="none" stroke="#6B429C" stroke-width="1.5"/><path d="M6.5 3.5v3h2" fill="none" stroke="#6B429C" stroke-width="1.3"/></svg>January 12,2022</div>
  <div class="card-title">Sed ut perspiciatis unde omnis iste natus error sit voluptatem</div>
  <p class="card-text">Lorem ipsum dolor sit amet, consectetur adipiscing elit, sed do eiusmod tempor</p>
  <a class="card-link">Learn More</a>
</article>
<article class="abs card" style="left:444px">
  <div class="card-date"><svg width="13" height="13" viewBox="0 0 13 13"><circle cx="6.5" cy="6.5" r="5.3" fill="none" stroke="#6B429C" stroke-width="1.5"/><path d="M6.5 3.5v3h2" fill="none" stroke="#6B429C" stroke-width="1.3"/></svg>January12,2022</div>
  <div class="card-title">Sed ut perspiciatis unde omnis iste natus error sit voluptatem</div>
  <p class="card-text">Lorem ipsum dolor sit amet, consectetur adipiscing elit, sed do eiusmod tempor</p>
  <a class="card-link">Learn More</a>
</article>
<article class="abs card" style="left:775px">
  <div class="card-date"><svg width="13" height="13" viewBox="0 0 13 13"><circle cx="6.5" cy="6.5" r="5.3" fill="none" stroke="#6B429C" stroke-width="1.5"/><path d="M6.5 3.5v3h2" fill="none" stroke="#6B429C" stroke-width="1.3"/></svg>January 12,2022</div>
  <div class="card-title">Sed ut perspiciatis unde omnis iste natus error sit voluptatem</div>
  <p class="card-text">Lorem ipsum dolor sit amet, consectetur adipiscing elit, sed do eiusmod tempor</p>
  <a class="card-link">Learn More</a>
</article>

<section class="contact">
  <svg class="abs icon" style="top:66px" width="26" height="26" viewBox="0 0 24 24"><path d="M6.6 10.8a15.1 15.1 0 0 0 6.6 6.6l2.2-2.2a1 1 0 0 1 1-.25 11.4 11.4 0 0 0 3.6.57 1 1 0 0 1 1 1V20a1 1 0 0 1-1 1A17 17 0 0 1 3 4a1 1 0 0 1 1-1h3.5a1 1 0 0 1 1 1c0 1.25.2 2.45.57 3.57a1 1 0 0 1-.25 1z" fill="#fff"/></svg>
  <div class="abs info" style="top:52px"><h4>555-014-2738</h4><p>Duis erat leo, aliquam laoreet fringilla quis, pretium vitae dui.</p></div>
  <svg class="abs icon" style="left:114px;top:177px" width="20" height="28" viewBox="0 0 20 28"><path d="M10 1a9 9 0 0 0-9 9c0 7 9 17 9 17s9-10 9-17a9 9 0 0 0-9-9z" fill="#fff"/><circle cx="10" cy="10" r="3.3" fill="#8869AF"/></svg>
  <div class="abs info" style="top:165px"><h4>Lorem ipsum</h4><p>Duis erat leo, aliquam laoreet fringilla quis, pretium vitae dui.</p></div>
  <svg class="abs icon" style="top:303px" width="31" height="24" viewBox="0 0 31 24"><rect x="1.5" y="1.5" width="28" height="21" fill="none" stroke="#fff" stroke-width="2.4"/><path d="M2 3l13.5 11L29 3" fill="none" stroke="#fff" stroke-width="2.4"/></svg>
  <div class="abs info" style="top:283px"><h4>hello@violetvale.example</h4><p>Duis erat leo, aliquam laoreet fringilla quis, pretium vitae dui.</p></div>

  <h3 class="abs form-title">How Can I Help You?</h3>
  <div class="abs field" style="left:558px;top:98px;width:257px;height:49px">Name</div>
  <div class="abs field" style="left:828px;top:98px;width:257px;height:49px">Phone</div>
  <div class="abs field" style="left:558px;top:159px;width:527px;height:49px">Email Adrees</div>
  <div class="abs field tall" style="left:558px;top:221px;width:527px;height:92px">Message</div>
  <div class="abs send">SEND</div>
</section>

<footer class="footer">
  <span class="abs" style="left:113px;top:37px">Murmur</span>
  <span class="abs" style="left:183px;top:37px">Circlet</span>
  <span class="abs" style="left:278px;top:37px">Lenscape</span>
  <span class="abs" style="right:113px;top:34px">© copyrights 2022 Violet Vale &nbsp;|&nbsp; All Rights Reserved</span>
</footer>

</body>
</html>
```